TBNW site redesign

Please redesign a home page with content provided. PSD only - no coding
Can use any images from Vexelmarq.com

Please create a site design that more clearly illustrates the client's services and expertise. We are looking for a high-end design.

Any images used must be generic or of Dallas TX.

Fonts: Any
Colors: Match to logo
Look: Modern - Professional

Target Market(s)

medium-large business owners

Number of Pages Required

1 page

Font styles to use
Serif
Sans Serif

Requirements
Must have
• cohesive professional design
• high end look
• Match to logo

```html
<!DOCTYPE html>
<html lang="en">
<head>
<meta charset="utf-8">
<title>TBNW Commercial Realty Group</title>
<link rel="stylesheet" href="https://fonts.googleapis.com/css2?family=Cinzel:wght@400;600;700&family=Lato:wght@400;700&display=swap">
<style>
:root{
  --red:#b5121b;
  --red-dark:#8c0c13;
  --red-deep:#6e0a10;
  --ink:#2b2b2b;
  --text:#555;
  --muted:#8a8a8a;
  --light:#f1f1f1;
  --gray:#e4e4e4;
  --footer:#3a3a3a;
  --white:#fff;
}
*{box-sizing:border-box;margin:0;padding:0}
html,body{width:1200px;height:5158px;overflow:hidden}
body{font-family:"Lato",Arial,sans-serif;color:var(--text);background:var(--white);position:relative}
section,header,footer{position:relative;width:1200px;overflow:hidden}
.abs{position:absolute}
.btn{display:inline-block;background:var(--red);color:var(--white);font-family:"Cinzel",Georgia,serif;font-weight:700;font-size:14px;letter-spacing:1px;padding:10px 20px;border:1px solid var(--white);white-space:nowrap}
.btn-sm{font-size:11px;padding:6px 12px}
.section-title{font-family:"Cinzel",Georgia,serif;font-weight:700;color:var(--red);font-size:40px;text-align:center;letter-spacing:1px}
.arrow{width:44px;height:44px;border-radius:50%;display:flex;align-items:center;justify-content:center}

/* hero */
.hero{height:740px;background:linear-gradient(180deg,#2c3a55 0%,#4b5a74 35%,#8c7a6a 62%,#c98a4a 78%,#3a2c2a 100%)}
.brand{left:137px;top:17px;width:208px;height:138px;background:var(--red);display:flex;align-items:center;justify-content:center;gap:12px}
.brand-square{width:22px;height:22px;background:var(--white)}
.brand-name{font-family:"Cinzel",Georgia,serif;font-weight:700;font-size:44px;color:var(--white)}
.socials{left:615px;top:25px;display:flex;gap:12px}
.socials span{width:36px;height:36px;border-radius:50%;border:2px solid var(--white);display:block}
.phone-pill{left:858px;top:22px;width:205px;height:42px;background:var(--red);border-radius:22px;display:flex;align-items:center;justify-content:center;gap:10px;color:var(--white);font-weight:700;font-size:22px}
.nav{left:392px;top:92px;display:flex;gap:34px}
.nav a{color:var(--white);text-decoration:none;font-family:"Cinzel",Georgia,serif;font-size:15px;font-weight:700;letter-spacing:1px;white-space:nowrap}
.nav a.active{border-bottom:2px solid var(--white);padding-bottom:4px}
.hero-box{left:316px;top:327px;width:586px;height:160px;background:rgba(150,16,24,.78);border:3px solid rgba(255,255,255,.8);outline:1px solid rgba(255,255,255,.5);outline-offset:6px;display:flex;flex-direction:column;align-items:center;justify-content:center;color:var(--white);font-family:"Cinzel",Georgia,serif;font-weight:700;white-space:nowrap}
.hero-box h1{font-size:31px;letter-spacing:1px}
.hero-box p{font-size:19px;margin-top:10px}
.hero .btn{left:525px;top:520px}
.hero .arrow{top:418px;background:var(--red)}

/* search */
.search{height:445px;background:var(--white)}
.search h2{position:absolute;top:58px;width:100%;text-align:center;font-family:"Cinzel",Georgia,serif;font-weight:700;font-size:20px;color:var(--ink)}
.search .sub{position:absolute;top:94px;width:100%;text-align:center;font-size:13px;color:var(--text);letter-spacing:1px}
.tab{top:158px;height:36px;font-family:"Cinzel",Georgia,serif;font-weight:700;font-size:14px;display:flex;align-items:center;justify-content:center}
.tab.on{left:463px;width:128px;background:var(--red);color:var(--white)}
.tab.off{left:630px;width:110px;color:var(--ink)}
.form-card{left:195px;top:192px;width:895px;height:190px;background:var(--white);box-shadow:0 6px 22px rgba(0,0,0,.15)}
.field{position:absolute;height:38px;border:1px solid #ccc;background:var(--white);font-size:14px;color:var(--muted);display:flex;align-items:center;padding:0 12px}
.range{left:388px;top:88px;width:260px}
.range .track{position:absolute;top:10px;width:260px;height:4px;background:#ddd}
.range .fill{position:absolute;top:10px;left:0;width:60px;height:4px;background:var(--red)}
.range .knob{position:absolute;top:3px;left:56px;width:4px;height:18px;background:var(--red)}
.range span{position:absolute;top:26px;font-size:12px;color:var(--ink)}
.search-btn{left:665px;top:86px;width:215px;height:40px;background:var(--red);color:var(--white);font-weight:700;font-size:14px;display:flex;align-items:center;justify-content:center;gap:8px}

/* about */
.about{height:500px}
.about .section-title{position:absolute;top:35px;width:100%}
.about-photo{left:137px;top:115px;width:428px;height:320px;border:3px solid var(--red);padding:10px}
.about-photo div{width:100%;height:100%;background:linear-gradient(135deg,#dfe3e8,#9aa6b2 60%,#4a4f58)}
.about-text{left:605px;top:125px;width:480px}
.about-text h3{font-family:"Cinzel",Georgia,serif;font-weight:700;font-size:17px;color:var(--ink);margin-bottom:14px;white-space:nowrap}
.about-text p{font-size:13.5px;line-height:27px;color:var(--text)}
.about .btn{left:605px;top:405px}

/* why */
.why{height:440px;background:linear-gradient(180deg,var(--red) 0%,var(--red-dark) 100%)}
.why .section-title{position:absolute;top:40px;width:100%;color:var(--white)}
.cards{position:absolute;left:133px;top:115px;display:flex;gap:45px}
.card{width:200px;height:275px;background:var(--white);text-align:center;padding:0 14px;position:relative}
.card-icon{width:74px;height:74px;margin:-12px auto 0;background:var(--red);display:flex;align-items:center;justify-content:center;border:3px solid var(--white);box-shadow:0 2px 6px rgba(0,0,0,.2)}
.card h4{font-family:"Cinzel",Georgia,serif;color:var(--red);font-size:13px;margin:26px 0 12px;white-space:nowrap}
.card p{font-size:11px;line-height:18px;color:var(--text);height:72px}
.card .btn{margin-top:14px}

/* calculator */
.calc{height:275px;background:linear-gradient(90deg,#d9d9d9 0%,#f3f3f3 35%,#f7f7f7 100%)}
.calc-art{left:0;top:0;width:390px;height:275px;background:linear-gradient(135deg,#c9c9c9,#eeeeee)}
.calc p{position:absolute;left:412px;top:50px;width:640px;text-align:center;font-family:"Cinzel",Georgia,serif;font-size:19px;line-height:34px;color:#666}
.calc .btn{left:620px;top:175px}

/* team */
.team{height:500px;background:linear-gradient(180deg,#fafafa,#f2f2f2)}
.team .section-title{position:absolute;top:48px;width:100%}
.members{position:absolute;left:144px;top:118px;display:flex;gap:34px}
.member{width:282px;height:362px;position:relative}
.member-photo{width:100%;height:268px}
.member-info{position:absolute;left:16px;right:16px;top:238px;height:112px;background:var(--red);text-align:center;color:var(--white);padding-top:16px;border:2px solid var(--white);outline:1px solid var(--red)}
.member-info h5{font-family:"Cinzel",Georgia,serif;font-size:13px;margin-bottom:10px}
.member-info p{font-size:12px;line-height:17px}

/* properties */
.props{height:570px;background:var(--gray)}
.props .section-title{position:absolute;top:70px;width:100%}
.prop-list{position:absolute;left:130px;top:130px;display:flex;gap:36px}
.prop{width:292px;text-align:center}
.prop-photo{width:292px;height:175px}
.prop p{font-size:13px;color:var(--ink);line-height:19px;margin:18px 8px 0;height:76px}
.prop .price{font-family:"Cinzel",Georgia,serif;font-weight:700;font-size:24px;color:var(--red);margin:0}
.prop .btn{margin-top:10px}
.props .arrow{top:255px;background:#c9c9c9}

/* testimonials */
.testi{height:385px;background:var(--white)}
.testi .section-title{position:absolute;top:38px;width:100%}
.avatar{left:560px;top:118px;width:80px;height:80px;border-radius:50%;border:3px solid var(--red);background:linear-gradient(135deg,#c9b8a6,#6f5a4a)}
.testi h5{position:absolute;top:214px;width:100%;text-align:center;font-family:"Cinzel",Georgia,serif;font-size:13px;color:var(--ink)}
.stars{position:absolute;top:234px;width:100%;text-align:center;color:var(--red);font-size:13px;letter-spacing:2px}
.testi .quote{position:absolute;left:250px;top:262px;width:700px;text-align:center;font-size:12.5px;line-height:21px;color:var(--muted)}
.qmark{position:absolute;top:270px;font-family:Georgia,serif;font-size:72px;color:#d9d9d9;line-height:1}

/* cta */
.cta{height:295px;background:linear-gradient(90deg,var(--red-dark),var(--red) 50%,var(--red-dark))}
.cta-art{right:0;top:0;width:420px;height:295px;background:linear-gradient(135deg,rgba(255,255,255,0) 0%,rgba(255,255,255,.08) 100%)}
.cta p{position:absolute;top:92px;width:100%;text-align:center;font-family:"Cinzel",Georgia,serif;font-weight:700;font-size:22px;line-height:34px;color:var(--white)}
.cta .btn{left:495px;top:190px;background:transparent}

/* articles */
.articles{height:385px;background:var(--white)}
.articles .section-title{position:absolute;top:60px;width:100%}
.article-list{position:absolute;left:130px;top:125px;display:flex;gap:36px}
.article{width:292px;height:140px;background:#f4f4f4;display:flex;gap:12px;padding:14px}
.article h6{font-size:14px;font-weight:400;color:var(--ink);line-height:20px;margin-bottom:10px}
.article-thumb{width:98px;height:110px;flex:none}
.articles .arrow{top:165px}

/* disclosure */
.disclosure{height:155px;background:var(--light);text-align:center;padding-top:32px}
.disclosure h6{font-family:"Cinzel",Georgia,serif;font-weight:700;font-size:21px;color:var(--red)}
.disclosure h6 small{font-family:"Lato",Arial,sans-serif;font-size:11px;color:var(--text);font-weight:400}
.disclosure a{display:block;color:var(--red);font-size:15px;margin-top:8px;text-decoration:underline}

/* footer */
.footer{height:378px;background:var(--footer);color:#ddd}
.footer h6{font-family:"Cinzel",Georgia,serif;font-size:19px;color:var(--white);font-weight:700;margin-bottom:22px;white-space:nowrap}
.col{position:absolute;top:58px}
.col ul{list-style:none}
.col li{font-size:12px;line-height:27px;color:#ddd}
.contact-row{display:flex;gap:10px;align-items:flex-start;font-size:13px;line-height:20px;margin-bottom:20px}
.pin{width:28px;height:28px;border-radius:50%;background:var(--red);flex:none;display:flex;align-items:center;justify-content:center}
.map{width:210px;height:190px;background:linear-gradient(135deg,#eaeaea,#cfd6d0)}
.foot-brand{width:210px;height:104px;background:var(--white);display:flex;align-items:center;justify-content:center;gap:10px}
.foot-brand .brand-square{background:var(--footer)}
.foot-brand .brand-name{color:var(--footer);font-size:38px}
.foot-social{display:flex;gap:12px;margin-top:22px;margin-left:20px}
.foot-social span{width:30px;height:30px;border-radius:50%;background:var(--red);display:block}
.copyright{height:50px;background:var(--red);color:var(--white);font-size:12px;letter-spacing:1px;display:flex;align-items:center;justify-content:center}
</style>
</head>
<body>

<header class="hero" role="img" aria-label="Dallas downtown skyline at dusk reflected in water">
  <div class="abs brand"><span class="brand-square"></span><span class="brand-name">TBNW</span></div>
  <div class="abs socials"><span></span><span></span><span></span><span></span></div>
  <div class="abs phone-pill">
    <svg width="20" height="20" viewBox="0 0 24 24"><path fill="#fff" d="M6.6 10.8a15.1 15.1 0 0 0 6.6 6.6l2.2-2.2c.3-.3.7-.4 1-.2 1.1.4 2.3.6 3.6.6.6 0 1 .4 1 1V20c0 .6-.4 1-1 1C10.6 21 3 13.4 3 4c0-.6.4-1 1-1h3.5c.6 0 1 .4 1 1 0 1.3.2 2.5.6 3.6.1.3 0 .7-.2 1z"/></svg>
    214-555-0148
  </div>
  <nav class="abs nav">
    <a class="active">HOME</a><a>ABOUT TBNW</a><a>SERVICES</a><a>BLOG</a><a>MARKET NEWS</a><a>CONTACT US</a>
  </nav>
  <div class="abs hero-box">
    <h1>PROFESSIONAL EXPERIENCED</h1>
    <p>AND OBJECTIVE COMMERCIAL REALTY GROUP</p>
  </div>
  <a class="abs btn">GET A QUOTE</a>
  <div class="abs arrow" style="left:46px"><svg width="16" height="16" viewBox="0 0 16 16"><path d="M11 2 5 8l6 6" stroke="#fff" stroke-width="2.5" fill="none"/></svg></div>
  <div class="abs arrow" style="left:1110px"><svg width="16" height="16" viewBox="0 0 16 16"><path d="m5 2 6 6-6 6" stroke="#fff" stroke-width="2.5" fill="none"/></svg></div>
</header>

<section class="search">
  <h2>PROFESSIONAL OFFICE AND WAREHOUSE LEASING</h2>
  <p class="sub">FAST TRACK YOUR SEARCH WITH TENANT REPS THAT ONLY SERVE YOU, AND SPECIALIZE IN THE DFW AREA</p>
  <div class="abs tab on">LEASE ESTATE</div>
  <div class="abs tab off">SALE ESTATE</div>
  <div class="abs form-card">
    <div class="field" style="left:12px;top:18px;width:580px">Search By Area</div>
    <div class="field" style="left:600px;top:18px;width:232px;justify-content:space-between">Office<svg width="10" height="6"><path d="M0 0h10L5 6z" fill="#888"/></svg></div>
    <div class="field" style="left:12px;top:86px;width:165px;justify-content:space-between">2000sqft<svg width="10" height="6"><path d="M0 0h10L5 6z" fill="#888"/></svg></div>
    <div class="field" style="left:185px;top:86px;width:165px;justify-content:space-between">Location<svg width="10" height="6"><path d="M0 0h10L5 6z" fill="#888"/></svg></div>
    <div class="abs range">
      <div class="track"></div><div class="fill"></div><div class="knob"></div>
      <span style="left:12px">$100</span><span style="right:0">$1,000,000</span>
    </div>
    <div class="abs search-btn">
      <svg width="14" height="14" viewBox="0 0 14 14"><circle cx="6" cy="6" r="4.5" stroke="#fff" stroke-width="2" fill="none"/><path d="m9.5 9.5 3.5 3.5" stroke="#fff" stroke-width="2"/></svg>SEARCH
    </div>
  </div>
</section>

<section class="about">
  <h2 class="section-title">ABOUT TBNW</h2>
  <div class="abs about-photo"><div role="img" aria-label="Business people shaking hands in an office"></div></div>
  <div class="abs about-text">
    <h3>LOREM IPSUM DOLOR SIT AMET, CONSECTETUR</h3>
    <p>Lorem ipsum dolor sit amet, consectetur adipiscing elit. Class aptent taciti sociosqu ad litora torquent per conubia nostra, per inceptos himenaeos. Donec porttitor ex quis lacus varius, ac molestie lectus commodo. Vivamus at sapien ante. Proin non ante sit amet neque porttitor iaculis non quis justo. Ut at fermentum enim. Suspendisse placerat vel nunc bibendum vehicula. Mauris ultricies faucibus quam, eget interdum massa finibus in.</p>
  </div>
  <a class="abs btn">READ MORE</a>
</section>

<section class="why">
  <h2 class="section-title">WHY TENANT REPRESENTATION</h2>
  <div class="cards">
    <div class="card">
      <div class="card-icon"><svg width="38" height="38" viewBox="0 0 38 38"><path d="M4 20l8-8 7 4 7-4 8 8-10 9-5-4-5 4z" fill="#fff"/></svg></div>
      <h4>RELATIONSHIP</h4>
      <p>We listen first, learn how your business works and stay beside you long after the lease is signed.</p>
      <a class="btn btn-sm">READ MORE</a>
    </div>
    <div class="card">
      <div class="card-icon"><svg width="38" height="38" viewBox="0 0 38 38"><rect x="6" y="6" width="26" height="26" fill="none" stroke="#fff" stroke-width="3"/><path d="M12 19h14M19 12v14" stroke="#fff" stroke-width="3"/></svg></div>
      <h4>ACCESS TO MORE</h4>
      <p>We know every landlord and broker in the market, so you see options others miss.</p>
      <a class="btn btn-sm">READ MORE</a>
    </div>
    <div class="card">
      <div class="card-icon"><svg width="38" height="38" viewBox="0 0 38 38"><circle cx="14" cy="16" r="7" fill="none" stroke="#fff" stroke-width="3"/><circle cx="26" cy="26" r="5" fill="none" stroke="#fff" stroke-width="3"/></svg></div>
      <h4>CUSTOMIZED SERVICE</h4>
      <p>Each search is built around your space, budget and timeline, never around a listing.</p>
      <a class="btn btn-sm">READ MORE</a>
    </div>
    <div class="card">
      <div class="card-icon"><svg width="38" height="38" viewBox="0 0 38 38"><circle cx="19" cy="19" r="12" fill="none" stroke="#fff" stroke-width="3"/><path d="M19 11v16M15 15h7M15 23h7" stroke="#fff" stroke-width="2.5"/></svg></div>
      <h4>FREE TO YOU</h4>
      <p>Our fees are paid by the landlord, so expert representation costs your company nothing.</p>
      <a class="btn btn-sm">READ MORE</a>
    </div>
  </div>
</section>

<section class="calc">
  <div class="abs calc-art" role="img" aria-label="Line drawing of a steel transmission tower"></div>
  <p>IF YOU NEED TO FIND OFFICE OR WAREHOUSE SPACE IN THE DALLAS FORT WORTH AREA, THE TEAM AT TBNW HAS THE EXPERIENCE YOU NEED.</p>
  <a class="abs btn">SPACE CALCULATOR</a>
</section>

<section class="team">
  <h2 class="section-title">MEET THE OUR TEAM</h2>
  <div class="members">
    <div class="member">
      <div class="member-photo" role="img" aria-label="Portrait of the founder in a grey suit" style="background:linear-gradient(180deg,#e9ecef,#a9b0b8)"></div>
      <div class="member-info"><h5>OWEN R. HARTWELL</h5><p>Founder<br>&amp; President</p></div>
    </div>
    <div class="member">
      <div class="member-photo" role="img" aria-label="Portrait of the senior director in a dark suit" style="background:linear-gradient(180deg,#3f4a57,#1e252d)"></div>
      <div class="member-info"><h5>DEAN COLVIN-ROSS</h5><p>Senior Director, Commercial<br>Property Specialist</p></div>
    </div>
    <div class="member">
      <div class="member-photo" role="img" aria-label="Portrait of the associate in a blazer" style="background:linear-gradient(180deg,#d8d8d8,#7c7c7c)"></div>
      <div class="member-info"><h5>NEIL ADRIAN FOSTER</h5><p>Associate, Tenant<br>Rep Specialist</p></div>
    </div>
  </div>
</section>

<section class="props">
  <h2 class="section-title">OUR PROPERTIES</h2>
  <div class="abs arrow" style="left:60px"><svg width="16" height="16" viewBox="0 0 16 16"><path d="M11 2 5 8l6 6" stroke="#fff" stroke-width="2.5" fill="none"/></svg></div>
  <div class="abs arrow" style="left:1096px"><svg width="16" height="16" viewBox="0 0 16 16"><path d="m5 2 6 6-6 6" stroke="#fff" stroke-width="2.5" fill="none"/></svg></div>
  <div class="prop-list">
    <div class="prop">
      <div class="prop-photo" role="img" aria-label="Open highway through desert land" style="background:linear-gradient(180deg,#8fb3d6 0%,#c9b89a 55%,#6c6258 100%)"></div>
      <p>Ridgeline Land For Sale, 900 County Road 40, Marlow Springs, Texas +/- 148.25 Acres</p>
      <div class="price">$30,730,055.40</div>
      <a class="btn btn-sm">VIEW DETAILS</a>
    </div>
    <div class="prop">
      <div class="prop-photo" role="img" aria-label="Office building exterior on a parkway" style="background:linear-gradient(180deg,#5a5a5a,#2e2e2e)"></div>
      <p>4820 Belmora Parkway<br>Office Sublease Northgate,<br>75099</p>
      <div class="price">$19.50</div>
      <a class="btn btn-sm">VIEW DETAILS</a>
    </div>
    <div class="prop">
      <div class="prop-photo" role="img" aria-label="Brick mid-rise office building" style="background:linear-gradient(180deg,#a9c3de 0%,#8a4a3a 50%,#5a2e24 100%)"></div>
      <p>Cedar Row / Uptown<br>Dallas Office<br>Sublease</p>
      <div class="price">$30,730,055.40</div>
      <a class="btn btn-sm">VIEW DETAILS</a>
    </div>
  </div>
</section>

<section class="testi">
  <h2 class="section-title">CLIENT TESTIMONIALS</h2>
  <div class="abs avatar" role="img" aria-label="Client portrait"></div>
  <h5>RAYMOND ELLIS CARTER</h5>
  <div class="stars">★★★★★</div>
  <span class="qmark" style="left:195px">&ldquo;</span>
  <span class="qmark" style="left:965px">&rdquo;</span>
  <p class="quote">The team at TBNW brings decades of experience in commercial real estate. They know which properties are about to become available before they are listed, and they have your back at the negotiating table. Thoughtful, patient and thorough, they found us the right office and saved us real money. You will not be disappointed.</p>
</section>

<section class="cta">
  <div class="abs cta-art" role="img" aria-label="House keys resting on paperwork"></div>
  <p>WHETHER YOUR LEASE IS EXPIRING SOON, OR YOU'RE JUST STARTING YOUR SEARCH,<br>TBNW CAN HELP YOU FIND THE PERFECT SPACE.</p>
  <a class="abs btn">MAKE AN APPOINTMENT</a>
</section>

<section class="articles">
  <h2 class="section-title">RECENT ARTICLES</h2>
  <div class="abs arrow" style="left:60px"><svg width="16" height="16" viewBox="0 0 16 16"><path d="M11 2 5 8l6 6" stroke="#999" stroke-width="2.5" fill="none"/></svg></div>
  <div class="abs arrow" style="left:1096px"><svg width="16" height="16" viewBox="0 0 16 16"><path d="m5 2 6 6-6 6" stroke="#999" stroke-width="2.5" fill="none"/></svg></div>
  <div class="article-list">
    <div class="article">
      <div><h6>6 Important Key Aspects Of Tenant Representation To Know!</h6><a class="btn btn-sm">READ MORE</a></div>
      <div class="article-thumb" role="img" aria-label="Business meeting at a table" style="background:linear-gradient(135deg,#d6d0c8,#8c8378)"></div>
    </div>
    <div class="article">
      <div><h6>How Does Landlord Recapture Relate To My Office Lease?</h6><a class="btn btn-sm">READ MORE</a></div>
      <div class="article-thumb" role="img" aria-label="Empty modern office interior" style="background:linear-gradient(135deg,#e4e4e4,#9ea4aa)"></div>
    </div>
    <div class="article">
      <div><h6>Do You Need Office Space? Don't Miss These Flexible Options!</h6><a class="btn btn-sm">READ MORE</a></div>
      <div class="article-thumb" role="img" aria-label="Shared workspace with desks" style="background:linear-gradient(135deg,#ececec,#b3b3b3)"></div>
    </div>
  </div>
</section>

<section class="disclosure">
  <h6>Texas Real Estate Commission Mandated Disclosure Notices <small>– click links below to view pages</small></h6>
  <a>Texas Real Estate Commission Information About Brokerage Services</a>
  <a style="margin-top:2px">Texas Real Estate Commission Consumer Protection Notice</a>
</section>

<footer class="footer">
  <div class="col" style="left:137px">
    <h6>QUICK LINKS</h6>
    <ul><li>HOME</li><li>ABOUT US</li><li>SERVICES</li><li>BLOG</li><li>MARKET NEWS</li><li>CONTACT US</li></ul>
  </div>
  <div class="col" style="left:320px;width:210px">
    <h6>CONTACT INFO</h6>
    <div class="contact-row"><span class="pin"><svg width="12" height="14" viewBox="0 0 12 14"><path d="M6 0a5 5 0 0 0-5 5c0 4 5 9 5 9s5-5 5-9a5 5 0 0 0-5-5z" fill="#fff"/></svg></span>410 Harwell Avenue,<br>Suite 300, Dallas, TX 75201</div>
    <div class="contact-row"><span class="pin"><svg width="14" height="14" viewBox="0 0 24 24"><path fill="#fff" d="M6.6 10.8a15.1 15.1 0 0 0 6.6 6.6l2.2-2.2c.3-.3.7-.4 1-.2 1.1.4 2.3.6 3.6.6.6 0 1 .4 1 1V20c0 .6-.4 1-1 1C10.6 21 3 13.4 3 4c0-.6.4-1 1-1h3.5c.6 0 1 .4 1 1 0 1.3.2 2.5.6 3.6.1.3 0 .7-.2 1z"/></svg></span>214-555-0148</div>
    <div class="contact-row"><span class="pin"><svg width="14" height="12" viewBox="0 0 14 12"><rect x="1" y="3" width="12" height="8" fill="#fff"/><rect x="3" y="0" width="8" height="3" fill="#fff"/></svg></span>214-555-0149</div>
  </div>
  <div class="col" style="left:570px">
    <h6>LOCATION MAP</h6>
    <div class="map" role="img" aria-label="Street map of the office location"></div>
  </div>
  <div class="col" style="left:852px">
    <h6>FOLLOWS US</h6>
    <div class="foot-brand"><span class="brand-square"></span><span class="brand-name">TBNW</span></div>
    <div class="foot-social"><span></span><span></span><span></span><span></span></div>
  </div>
</footer>
<div class="copyright">© COPYRIGHT 2018 TBNW. ALL RIGHT RESERVED</div>

</body>
</html>
```